Crafting Magic: Design the Next Funky Brand of Magic Chocolate and Gummies

Introduction:
Welcome to our ZippyMorrow Design Challenge! We're on a quest to discover the next big thing in magical treats, and we need your creativity to make it happen. Are you ready to delve into the world of enchanting flavors and whimsical designs? Join us as we embark on a journey to create the most captivating brand of magic chocolate and gummies ever seen.
Objective:
The objective of this contest is to design a brand concept around the name ZippyMorrow for magic chocolate and magic gummies that embodies the spirit of Fun, Nature, and Enchantment. We're looking for unique and eye-catching designs that will captivate consumers and transport them to a world of wonder with each bite.
Brand Inspiration:
Imagine a world where every bite is a magical experience. We love to say that Nature is Intelligent. Think natural and organic vibrant colors, fantastical creatures coming out of the Woods, and whimsical packaging that sparks joy and excitement. Whether it's a Orvane inspired world, magic beings that jumps with flavor or gummies that fizz and sparkle, let your imagination run wild and create a brand that stands out from the crowd.
Brand benchmark : Pemblow
Guidelines:
1. Theme: Your design should revolve around the concept of Nature, Magic and enchantment. Think about what magic means to you and how you can incorporate it into the branding of your chocolate and gummies.
2. Brand Identity: Develop a unique brand logo, and tagline that capture the essence of your magical treats. Consider the target audience and what will appeal to them.
3. Packaging Design: Create packaging designs for both the magic chocolate and magic gummies that are visually stunning and cohesive with your brand identity. Think about how the packaging will stand out on shelves and online.
4. Flavor Profiles: Describe the flavors of your magic chocolate and gummies. Get creative with exotic ingredients and spellbinding combinations that will tantalize the taste buds.
5. Marketing Strategy: Outline a marketing strategy for launching your brand online. How will you create buzz and attract customers to try your magical treats? Consider social media campaigns, influencer partnerships, and other promotional tactics.
Requirements
Must have
- It has to be discrete and not obvious for customs, to avoid products being seized, Name : ZippyMorrow - Chocolate bars with 3 iterations (3 tastes) and same for Gummies pouches (doypack zip bags)
Nice to have
- Organic / Nature inspired / Orvane inspired Gummies
Should not have
- A copy Paste of our inspiration brand called Pemblow

```html
<!DOCTYPE html>
<html lang="en">
<head>
<meta charset="utf-8">
<title>ZippyMorrow – A Bite Of chocolate bar wrappers</title>
<link href="https://fonts.googleapis.com/css2?family=Fraunces:opsz,wght@9..144,800&family=Montserrat:wght@300;400;600;800&display=swap" rel="stylesheet">
<style>
  :root {
    --page: #e6eafc;
    --wrapper: #1a1ea0;
    --wrapper-fold: #24329f;
    --wrapper-rule: #3a48c4;
    --ink: #ffffff;
    --trim: #111111;
    --green: #7cf01c;
    --magenta: #e03be6;
    --yellow: #f2d21b;
  }
  * { box-sizing: border-box; margin: 0; padding: 0; }
  html, body { width: 849px; height: 1200px; overflow: hidden; }
  body {
    background: var(--page);
    font-family: "Montserrat", sans-serif;
    color: var(--ink);
    position: relative;
  }
  .dieline {
    position: absolute;
    left: 125px;
    width: 600px;
    height: 370px;
  }
  .dieline--moon { top: 15px; --accent: var(--green); }
  .dieline--nebula { top: 405px; --accent: var(--magenta); }
  .dieline--starglow { top: 795px; --accent: var(--yellow); }

  .trim-frame {
    position: absolute; left: 48px; top: 18px; width: 540px; height: 290px;
    border: 1px solid var(--trim);
  }
  .crop { position: absolute; background: var(--trim); }
  .crop--v { width: 1px; top: 0; height: 32px; }
  .crop--h { height: 1px; left: 28px; width: 34px; }
  .measure {
    position: absolute; left: 36px; width: 14px;
    display: flex; align-items: center; justify-content: center;
    font-size: 8px; color: var(--trim);
  }
  .measure span { transform: rotate(-90deg); white-space: nowrap; }
  .fold-note {
    position: absolute; left: 48px; width: 540px; top: 312px;
    text-align: center; font-size: 8px; color: var(--trim);
  }

  .wrapper {
    position: absolute; left: 62px; top: 32px; width: 510px; height: 263px;
    background: var(--wrapper);
    overflow: hidden;
  }
  .band { position: absolute; left: 0; width: 100%; border-bottom: 1px solid var(--wrapper-rule); }
  .band--back { top: 0; height: 76px; }
  .band--front { top: 76px; height: 108px; }
  .band--story { top: 184px; height: 59px; }
  .band--fold { top: 243px; height: 20px; background: var(--wrapper-fold); border-bottom: 0; }

  .nutrition { position: absolute; left: 28px; top: 9px; width: 140px; font-size: 4.6px; line-height: 1.3; }
  .nutrition b { font-weight: 800; }
  .nutrition dl { display: grid; grid-template-columns: 48px 1fr; }
  .organic { position: absolute; left: 172px; top: 8px; font-size: 6.5px; font-weight: 800; }
  .organic small { display: block; font-size: 4.5px; font-weight: 400; font-style: italic; margin-top: 3px; }
  .seal {
    position: absolute; left: 200px; top: 30px; width: 36px; height: 42px;
    border: 1px solid var(--ink); border-radius: 18px 18px 2px 2px;
  }
  .brand {
    position: absolute; font-family: "Fraunces", serif; font-weight: 800;
    color: var(--accent); white-space: nowrap; text-align: center;
  }
  .band--back .brand { right: 22px; top: 10px; font-size: 8px; }
  .band--front .brand { right: 22px; top: 50px; font-size: 7px; }
  .brand::before {
    content: ""; display: block; width: 34px; height: 34px; margin: 0 auto 3px;
    border: 1px solid var(--accent); border-radius: 50%;
  }
  .band--front .brand::before { width: 28px; height: 28px; }

  .artwork {
    position: absolute; left: 250px; top: 6px; width: 170px; height: 96px;
    background: radial-gradient(ellipse at center, rgba(90,110,220,0.35), rgba(26,30,160,0) 70%);
  }
  .kicker {
    position: absolute; left: 28px; top: 10px;
    font-size: 9px; font-weight: 300; letter-spacing: 0.5px;
    display: flex; align-items: center; gap: 4px;
  }
  .kicker::after { content: ""; width: 58px; height: 1px; background: var(--ink); }
  .flavour {
    position: absolute; left: 26px; top: 22px;
    font-family: "Fraunces", serif; font-weight: 800;
    color: var(--accent); font-size: 32px; line-height: 0.95;
  }
  .flavour--single { top: 30px; }
  .flavour .indent { display: block; padding-left: 38px; }
  .bar-type {
    position: absolute; left: 270px; top: 88px; font-size: 6.5px; letter-spacing: 0.3px;
    display: flex; align-items: center; gap: 4px;
  }
  .bar-type::before { content: ""; width: 14px; height: 1px; background: var(--accent); }
  .bar-type b { color: var(--accent); font-weight: 800; }

  .story {
    position: absolute; left: 50px; right: 50px; top: 50%; transform: translateY(-50%);
    text-align: center; font-size: 4.8px; font-weight: 600; line-height: 1.4;
  }
</style>
</head>
<body>

<section class="dieline dieline--moon">
  <div class="crop crop--v" style="left:62px"></div>
  <div class="crop crop--v" style="left:572px"></div>
  <div class="crop crop--h" style="top:32px"></div>
  <div class="crop crop--h" style="top:108px"></div>
  <div class="crop crop--h" style="top:216px"></div>
  <div class="crop crop--h" style="top:275px"></div>
  <div class="crop crop--h" style="top:295px"></div>
  <div class="measure" style="top:32px;height:76px"><span>31mm</span></div>
  <div class="measure" style="top:108px;height:108px"><span>44mm</span></div>
  <div class="measure" style="top:216px;height:59px"><span>24mm</span></div>
  <div class="measure" style="top:275px;height:20px;font-size:5px"><span>8mm</span></div>
  <div class="trim-frame"></div>
  <div class="wrapper">
    <div class="band band--back">
      <div class="nutrition">
        <b>Ingredients:</b> raw cocoa, cocoa butter, proprietary adaptogenic blend, and lots of love.<br>
        <b>Nutrition facts:</b>
        <dl><dt>Energy (kcal)</dt><dd>571 kcal</dd><dt>Fat</dt><dd>40 g</dd><dt>Saturates</dt><dd>24 g</dd><dt>Carbohydrates</dt><dd>14,6 g</dd><dt>Sugar</dt><dd>11 g</dd><dt>Protein</dt><dd>2,1 g</dd><dt>Salt</dt><dd>0 g</dd><dt>Fibre</dt><dd>2,4 g</dd></dl>
      </div>
      <p class="organic">Organic Raw Chocolate<small>*Do not swallow. Do not consume.</small></p>
      <div class="seal" role="img" aria-label="Quality seal"></div>
      <p class="brand">ZIPPYMORROW</p>
    </div>
    <div class="band band--front">
      <div class="artwork" role="img" aria-label="Faint line illustration of a chocolate bar, lollipop and leaves"></div>
      <p class="kicker">A BITE OF</p>
      <h2 class="flavour">MOON<span class="indent">TRAIL</span></h2>
      <p class="bar-type"><b>DARK</b> CHOCOLATE BAR</p>
      <p class="brand">ZIPPYMORROW</p>
    </div>
    <div class="band band--story">
      <p class="story">"Moon Trail" is a dreamy chocolate shaped by quiet forests and silver light.<br>Each square melts slowly, like a soft path of moonlight over the ferns. Deep dark cocoa meets a gentle<br>crunch, keeping time with owls calling from the branches and the hush of the night breeze<br>through the leaves. Every piece feels like a small charm, every note a whisper of sweetness,<br>and every moment a stroll through a hidden glade under the stars... Wake the wild within!</p>
    </div>
    <div class="band band--fold"></div>
  </div>
  <p class="fold-note">Naar binnen gevouwen</p>
</section>

<section class="dieline dieline--nebula">
  <div class="crop crop--v" style="left:62px"></div>
  <div class="crop crop--v" style="left:572px"></div>
  <div class="crop crop--h" style="top:32px"></div>
  <div class="crop crop--h" style="top:108px"></div>
  <div class="crop crop--h" style="top:216px"></div>
  <div class="crop crop--h" style="top:275px"></div>
  <div class="crop crop--h" style="top:295px"></div>
  <div class="measure" style="top:32px;height:76px"><span>31mm</span></div>
  <div class="measure" style="top:108px;height:108px"><span>44mm</span></div>
  <div class="measure" style="top:216px;height:59px"><span>24mm</span></div>
  <div class="measure" style="top:275px;height:20px;font-size:5px"><span>8mm</span></div>
  <div class="trim-frame"></div>
  <div class="wrapper">
    <div class="band band--back">
      <div class="nutrition">
        <b>Ingredients:</b> raw cocoa, cocoa butter, proprietary adaptogenic blend, and lots of love.<br>
        <b>Nutrition facts:</b>
        <dl><dt>Energy (kcal)</dt><dd>571 kcal</dd><dt>Fat</dt><dd>40 g</dd><dt>Saturates</dt><dd>24 g</dd><dt>Carbohydrates</dt><dd>14,6 g</dd><dt>Sugar</dt><dd>11 g</dd><dt>Protein</dt><dd>2,1 g</dd><dt>Salt</dt><dd>0 g</dd><dt>Fibre</dt><dd>2,4 g</dd></dl>
      </div>
      <p class="organic">Organic Raw Chocolate<small>*Do not swallow. Do not consume.</small></p>
      <div class="seal" role="img" aria-label="Quality seal"></div>
      <p class="brand">ZIPPYMORROW</p>
    </div>
    <div class="band band--front">
      <div class="artwork" role="img" aria-label="Faint line illustration of a chocolate bar, lollipop and leaves"></div>
      <p class="kicker">A BITE OF</p>
      <h2 class="flavour flavour--single">NEBULA</h2>
      <p class="bar-type"><b>DARK</b> CHOCOLATE BAR</p>
      <p class="brand">ZIPPYMORROW</p>
    </div>
    <div class="band band--story">
      <p class="story">"Nebula" is a chocolate that gathers the glow of faraway clouds of light,<br>blending wonder, mystery, the forest floor and sweetness. Every bite drifts like a voyage past bright planets,<br>a swirl of celestial flavours. Dark cocoa, bold and velvety, recalls the deep blue of the open sky,<br>while warm earthy notes hold the comfort of a campfire under the night sky... Wake the wild within!</p>
    </div>
    <div class="band band--fold"></div>
  </div>
  <p class="fold-note">Naar binnen gevouwen</p>
</section>

<section class="dieline dieline--starglow">
  <div class="crop crop--v" style="left:62px"></div>
  <div class="crop crop--v" style="left:572px"></div>
  <div class="crop crop--h" style="top:32px"></div>
  <div class="crop crop--h" style="top:108px"></div>
  <div class="crop crop--h" style="top:216px"></div>
  <div class="crop crop--h" style="top:275px"></div>
  <div class="crop crop--h" style="top:295px"></div>
  <div class="measure" style="top:32px;height:76px"><span>31mm</span></div>
  <div class="measure" style="top:108px;height:108px"><span>44mm</span></div>
  <div class="measure" style="top:216px;height:59px"><span>24mm</span></div>
  <div class="measure" style="top:275px;height:20px;font-size:5px"><span>8mm</span></div>
  <div class="trim-frame"></div>
  <div class="wrapper">
    <div class="band band--back">
      <div class="nutrition">
        <b>Ingredients:</b> raw cocoa, cocoa butter, proprietary adaptogenic blend, and lots of love.<br>
        <b>Nutrition facts:</b>
        <dl><dt>Energy (kcal)</dt><dd>571 kcal</dd><dt>Fat</dt><dd>40 g</dd><dt>Saturates</dt><dd>24 g</dd><dt>Carbohydrates</dt><dd>14,6 g</dd><dt>Sugar</dt><dd>11 g</dd><dt>Protein</dt><dd>2,1 g</dd><dt>Salt</dt><dd>0 g</dd><dt>Fibre</dt><dd>2,4 g</dd></dl>
      </div>
      <p class="organic">Organic Raw Chocolate<small>*Do not swallow. Do not consume.</small></p>
      <div class="seal" role="img" aria-label="Quality seal"></div>
      <p class="brand">ZIPPYMORROW</p>
    </div>
    <div class="band band--front">
      <div class="artwork" role="img" aria-label="Faint line illustration of a chocolate bar, lollipop and leaves"></div>
      <p class="kicker">A BITE OF</p>
      <h2 class="flavour flavour--single">STARGLOW</h2>
      <p class="bar-type"><b>DARK</b> CHOCOLATE BAR</p>
      <p class="brand">ZIPPYMORROW</p>
    </div>
    <div class="band band--story">
      <p class="story">"Starglow" is a dark chocolate, bold and deep, that lifts the curtain on the night sky,<br>calling you to wander through its glittering heights.<br>The flavour flickers across the tongue like a tiny spark of wonder, waking<br>every sense with bright, lively energy. In each square there is a hint of gentle sweetness, like dew on a<br>field of wild herbs at dawn, softening the bold depth of the cocoa.<br>Each piece of "Starglow" carries a little spell, as though every bite were a trip<br>across a sky full of marvels and flavour... Wake the wild within!</p>
    </div>
    <div class="band band--fold"></div>
  </div>
  <p class="fold-note">Naar binnen gevouwen</p>
</section>

</body>
</html>
```